Ridexa Academy Wordpress Motorcycle School Business Website

We are a motorcycle training school that is located in Calgary, AB, Canada. Our main service is motorcycle safety training. We currently have a site at www.ridexaacademy-example.com . We would like to see a design whereby the colours align with our logo (a white background is best), as well as effectively communicating our strengths as a school and the value and quality of the services we provide.

There are also photos on our facebook page at: www.facebook.com/ridexaacademyexample/ , it would be nice to incorporate some, but we are open to using generic photos as well.

It is important that the entire site be mobile friendly. The front page should be able to house all the information that a potential student would be looking for in terms of WHY they should choose us, without having to navigate to secondary pages.

We also currently have a small youtube clip that we would like to keep on the main page to "hook" a potential customer. We have secondary pages in our menu for further details and also have an integrated booking engine on one of the pages so that student's can book and pay online. These things we would like to keep. It would also be nice to give the ability for our customers to share the website's pages on social media.

Our current subpages are:
About Us
Our Staff
Our Fleet
Client Testimonials
Friends of Ridexa
Course Descriptions
Course Pricing
Bookings (where they book)
FAQ
Privacy Policy
Contact Page

A more efficient and effective method of organizing/delivering the content would be great.

Finally... a sleek, modern/contemporary theme is what we are after. Our company slogan being: Fun - Safe - Professional

Please reference the existing website for all the necessary content.

Target Market(s)

18-50 year old. Motorcycle enthusiast students who want to learn to ride.

Industry/Entity Type

Driving School

Font styles to use
Sans Serif

Requirements
Must have
• Some photos from our facebook page would be great.
• Ridexa Academy Logo colours
• Please refer to the Project Description.
Nice to have
• Modern/Contemporary

```html
<!DOCTYPE html>
<html lang="en">
<head>
<meta charset="utf-8">
<title>Ridexa Academy – Motorcycle Training</title>
<link rel="stylesheet" href="https://fonts.googleapis.com/css2?family=Open+Sans:ital,wght@0,400;0,600;0,700;1,600&family=Oswald:wght@400;500&display=swap">
<style>
:root{
  --yellow:#f6b80f;
  --orange:#e9a000;
  --ink:#222;
  --text:#555;
  --dark:#1c1c1c;
  --darker:#141414;
  --nav:#111;
  --line:#e3e3e3;
  --light:#f4f4f4;
  --white:#fff;
}
*{box-sizing:border-box;margin:0;padding:0}
html,body{width:1200px;height:2896px;overflow:hidden}
body{font-family:"Open Sans",Arial,sans-serif;color:var(--text);background:var(--white);font-size:13px;line-height:1.6;position:relative}
.wrap{width:1110px;margin:0 auto;position:relative}
.btn{display:inline-block;background:var(--yellow);color:var(--ink);font-weight:700;font-size:11px;letter-spacing:.5px;padding:7px 16px;text-transform:uppercase;line-height:1.4}
.btn-light{background:var(--white);color:var(--ink)}
h2.section-title{font-family:"Oswald",Arial,sans-serif;font-weight:400;color:var(--orange);text-align:center;font-size:32px;line-height:1.2}

/* header */
.site-header{position:absolute;top:0;left:0;width:1200px;height:90px;background:var(--white);z-index:2}
.logo{position:absolute;left:44px;top:18px;display:flex;align-items:center;gap:10px}
.logo-mark{width:44px;height:44px;border-radius:50%;background:var(--yellow)}
.logo-name{font-weight:700;font-size:30px;color:var(--ink);letter-spacing:.5px}
.util-nav{position:absolute;right:0;top:0;display:flex;background:var(--nav)}
.util-nav a{color:#ddd;font-size:12px;padding:7px 18px;text-decoration:none}
.util-nav a.current{background:var(--yellow);color:var(--ink);font-weight:600}

/* hero */
.hero{position:absolute;top:90px;left:0;width:1200px;height:380px;background:linear-gradient(180deg,#c9d4db 0%,#9aa3a7 45%,#6f726c 75%,#4b4a44 100%)}
.hero-slogan{position:absolute;top:130px;width:100%;text-align:center;color:var(--white);font-family:"Oswald",Arial,sans-serif;font-size:54px;font-style:italic;letter-spacing:1px;text-shadow:0 2px 8px rgba(0,0,0,.35)}

/* main nav */
.main-nav{position:absolute;top:470px;left:0;width:1200px;height:44px;background:var(--nav)}
.main-nav ul{list-style:none;display:flex;height:44px;margin-left:104px}
.main-nav li{color:#eee;font-size:12px;font-weight:600;padding:0 20px;line-height:44px}
.main-nav li.active{background:var(--yellow);color:var(--ink)}
.search-btn{position:absolute;right:104px;top:7px;width:30px;height:30px;background:var(--yellow);display:flex;align-items:center;justify-content:center}

/* welcome */
.welcome{position:absolute;top:514px;left:0;width:1200px;height:236px;padding-top:26px;text-align:center}
.welcome h1{font-family:"Oswald",Arial,sans-serif;font-weight:400;font-size:24px;color:var(--ink);letter-spacing:.5px;line-height:1.3}
.welcome h1 span{color:var(--orange)}
.welcome p{width:1000px;margin:12px auto 16px;font-size:12.5px;text-align:left}

/* courses */
.courses{position:absolute;top:750px;left:0;width:1200px;height:322px;background:linear-gradient(180deg,#2a2a2a,#3c3733 60%,#262321)}
.courses h2{color:var(--yellow);text-align:center;font-family:"Oswald",Arial,sans-serif;font-weight:400;font-size:28px;line-height:1.2;padding-top:16px}
.course-list{display:flex;justify-content:space-between;width:960px;margin:12px auto 0}
.course{width:290px;text-align:center;color:#ccc}
.course-icon{width:52px;height:52px;border-radius:50%;background:var(--yellow);margin:0 auto 6px;display:flex;align-items:center;justify-content:center}
.course h3{color:var(--yellow);font-size:16px;font-weight:600;line-height:1.25;margin-bottom:5px}
.course p{font-size:11.5px;line-height:1.5;margin-bottom:8px;height:51px;overflow:hidden}
.course-actions{position:absolute;left:0;bottom:14px;width:100%;text-align:center}
.course-actions .btn{margin:0 4px}

/* compare */
.compare{position:absolute;top:1072px;left:0;width:1200px;height:416px;padding-top:30px}
.compare table{width:1110px;margin:22px auto 0;border-collapse:collapse;font-size:11.5px}
.compare th{background:var(--yellow);color:var(--ink);text-align:left;padding:8px 12px;font-size:11px;text-transform:uppercase;font-weight:700}
.compare td{padding:6px 12px;border-bottom:1px solid var(--line);color:#444}
.compare tr:nth-child(even) td{background:var(--light)}
.compare td:first-child{width:34%}

/* video */
.video-feature{position:absolute;top:1488px;left:0;width:1200px;height:372px;background:linear-gradient(180deg,#2b2b2b,#1d1d1d)}
.video-player{position:absolute;left:45px;top:40px;width:520px;height:292px;background:linear-gradient(180deg,#b9c4c9,#7d8580 60%,#5a5d55)}
.video-bar{position:absolute;left:0;bottom:0;width:100%;height:26px;background:rgba(0,0,0,.75);display:flex;align-items:center;padding:0 10px;gap:10px}
.video-progress{flex:1;height:4px;background:#555}
.video-progress span{display:block;width:35%;height:4px;background:var(--yellow)}
.video-text{position:absolute;left:600px;top:40px;width:555px;color:#ccc}
.video-text h2{font-family:"Oswald",Arial,sans-serif;font-weight:400;color:var(--white);font-size:26px;line-height:1.3;margin-bottom:10px}
.video-text p{font-size:12px;margin-bottom:10px}

/* blog */
.blog{position:absolute;top:1860px;left:0;width:1200px;height:400px;padding-top:30px}
.blog-list{display:flex;justify-content:space-between;margin-top:22px}
.post{width:350px}
.post h3{font-size:15px;font-weight:600;color:var(--ink);line-height:1.35;margin-bottom:10px}
.post p{font-size:12px;margin-bottom:14px}

/* stories */
.stories{position:absolute;top:2260px;left:0;width:1200px;height:348px;background:var(--light);padding-top:26px}
.story{display:flex;gap:30px;margin-top:22px}
.story-photo{width:430px;height:210px;background:linear-gradient(180deg,#c7d6e2,#9fb0a0 55%,#6d7a5e);flex:none}
.story-text h3{font-size:15px;font-weight:600;color:var(--ink);margin-bottom:10px}
.story-text p{font-size:12px;margin-bottom:12px}

/* footer */
.site-footer{position:absolute;top:2608px;left:0;width:1200px;height:288px;background:var(--dark);color:#aaa}
.footer-cols{display:flex;justify-content:space-between;padding-top:28px}
.footer-col{width:250px;font-size:12px}
.footer-col h4{color:var(--white);font-size:16px;font-weight:600;margin-bottom:12px}
.footer-col ul{list-style:none;line-height:1.75}
.social{display:flex;gap:8px}
.social span{width:24px;height:24px;border-radius:50%;background:#555}
.social span:nth-child(1){background:#3b5998}.social span:nth-child(2){background:#1da1f2}
.social span:nth-child(3){background:#dd4b39}.social span:nth-child(4){background:#0e76a8}
.social span:nth-child(5){background:var(--yellow)}.social span:nth-child(6){background:#c4302b}
.footer-form{display:flex;margin-top:10px}
.footer-form .field{flex:1;height:28px;background:var(--white);color:#999;font-size:11px;padding:6px 8px}
.footer-form .btn{padding:7px 12px}
.footer-bottom{position:absolute;bottom:0;left:0;width:1200px;height:34px;background:var(--darker);font-size:11px;color:#888}
.footer-bottom .wrap{display:flex;justify-content:space-between;line-height:34px}
</style>
</head>
<body>

<header class="site-header">
  <div class="logo"><span class="logo-mark"></span><span class="logo-name">Ridexa</span></div>
  <nav class="util-nav">
    <a class="current">Course Information</a><a>Course Pricing</a><a>Bookings</a><a>Privacy Policy</a>
  </nav>
</header>

<section class="hero" role="img" aria-label="Photo of a smiling rider on a motorcycle on the training lot with other students and bikes behind">
  <p class="hero-slogan">" Fun - Safe - Professional "</p>
</section>

<nav class="main-nav">
  <ul>
    <li class="active">Home</li><li>About Us</li><li>Our Staff</li><li>Our Fleet</li><li>Client Testimonials</li><li>Friends of Ridexa</li>
  </ul>
  <span class="search-btn"><svg width="14" height="14" viewBox="0 0 14 14"><circle cx="6" cy="6" r="4.2" fill="none" stroke="#222" stroke-width="1.8"/><line x1="9" y1="9" x2="13" y2="13" stroke="#222" stroke-width="1.8"/></svg></span>
</nav>

<section class="welcome">
  <h1>WELCOME TO <span>RIDEXA ACADEMY</span></h1>
  <p>Our students learn about Ridexa Academy because we are of high quality, great value, and enthusiastically professional. We believe in the essence of safe motorcycling and proper instruction. Although we know that we can not make you an expert rider after years of experience would in one course, we can provide you with a solid foundation of skills, techniques and knowledge, which will keep you safer and get you ready for the wonderful world of motorcycles. Simply put, we use strategy that is based on building rider confidence at a comfortable pace, and we have built the course from the ground up with safety and fun in mind.</p>
  <span class="btn">Read more</span>
</section>

<section class="courses" role="img" aria-label="Dim photo of the school garage with parked training motorcycles behind the course list">
  <h2>Courses</h2>
  <div class="course-list">
    <div class="course">
      <div class="course-icon"><svg width="24" height="24" viewBox="0 0 26 26"><circle cx="13" cy="11" r="6" fill="none" stroke="#fff" stroke-width="2"/><rect x="10" y="18" width="6" height="4" fill="#fff"/></svg></div>
      <h3>Ridexa Basic</h3>
      <p>The Basic course is for new riders with limited experience. Learn control, balance and traffic awareness on our private lot.</p>
      <span class="btn">Read more</span>
    </div>
    <div class="course">
      <div class="course-icon"><svg width="24" height="24" viewBox="0 0 26 26"><path d="M5 13a8 8 0 1 1 2.3 5.7" fill="none" stroke="#fff" stroke-width="2"/><path d="M3 18l4 1 1-4" fill="none" stroke="#fff" stroke-width="2"/></svg></div>
      <h3>Ridexa Refresher</h3>
      <p>The Refresher course is for riders who have been away from the saddle. Rebuild your skills and confidence quickly.</p>
      <span class="btn">Read more</span>
    </div>
    <div class="course">
      <div class="course-icon"><svg width="24" height="24" viewBox="0 0 26 26"><path d="M3 8l10-4 10 4-10 4z" fill="#fff"/><path d="M7 10v6c3 3 9 3 12 0v-6" fill="none" stroke="#fff" stroke-width="2"/></svg></div>
      <h3>Ridexa Rider Proficiency Training</h3>
      <p>Advanced proficiency training for riders who want to sharpen their technique and ride with more skill on the road.</p>
      <span class="btn">Read more</span>
    </div>
  </div>
  <div class="course-actions"><span class="btn">Book now</span><span class="btn btn-light">View our fleet</span></div>
</section>

<section class="compare">
  <h2 class="section-title">Why choose us? What makes us different from others?</h2>
  <table>
    <tr><th>Description</th><th>Ridexa Academy</th><th>"Other Training Schools"</th></tr>
    <tr><td>Licensed by Northvale Rider Licensing Board</td><td>Yes</td><td>No</td></tr>
    <tr><td>Student Instructor Ratio</td><td>3:1</td><td>6:1 +</td></tr>
    <tr><td>Maximum Class Size</td><td>6</td><td>12</td></tr>
    <tr><td>Training Lot</td><td>Dedicated private lot, open all season</td><td>Shared parking lot</td></tr>
    <tr><td>Classroom Facilities</td><td>Modern classroom with video and models</td><td>Improvised room, no media</td></tr>
    <tr><td>Instructors</td><td>Certified, experienced and friendly riders</td><td>Sometimes certified</td></tr>
    <tr><td>Motorcycles</td><td>Newer, well kept fleet of all sizes</td><td>Older, mixed bikes</td></tr>
    <tr><td>Riding Gear</td><td>Helmets and gloves supplied free</td><td>Bring your own gear</td></tr>
    <tr><td>Road Test</td><td>Road test booked for you on-site</td><td>Not available, no help</td></tr>
  </table>
</section>

<section class="video-feature">
  <div class="video-player" role="img" aria-label="Video still of a student rider leaning through a turn on the training course">
    <div class="video-bar">
      <svg width="12" height="12" viewBox="0 0 12 12"><path d="M2 1l9 5-9 5z" fill="#fff"/></svg>
      <div class="video-progress"><span></span></div>
      <svg width="14" height="12" viewBox="0 0 14 12"><path d="M1 4h3l4-3v10l-4-3H1z" fill="#fff"/></svg>
    </div>
  </div>
  <div class="video-text">
    <h2>At vero accusam invidunt</h2>
    <p>Lorem ipsum dolor sit amet, te ex nostrum dignissim aliquam. Nihil verear voluptua ad per, quo soleat oporteat apeirian ex, amet senserit indoctum cu ut est munere sanctus.</p>
    <p>Cum purto recteque deterruisset id, sed putant tincidunt in. Per mollis liberavisse ut, eu vix assum eripuit, nam eu legere graecis erroribus. Mei dicant eripuit ei, et sit errem ornatus scriptorem, mei ne fierent mentitum. Sed ut dicta omnium tacimates, vim ut elit quas efficiendi.</p>
    <p>Quo noluisse pertinax voluptatibus et, no nec quem elit etiam. Est id clita inani suscipiantur, eum ad accusata definitiones. Vim noster labitur ut, mea cu ipsum sonet.</p>
    <span class="btn">Read more</span>
  </div>
</section>

<section class="blog">
  <div class="wrap">
    <h2 class="section-title">Blog</h2>
    <div class="blog-list">
      <article class="post">
        <h3>Quam nihil facilis qui ad, malorum veritus graecis an per mundi. Ius te</h3>
        <p>Partem melius pertinacia et sed, no vero aliquam fabulas. Summo vocibus scripserit ex vel, per recteque ancillae eu. Quo nemore menandri complectitur no, quas eloquentiam ad quo. Ne has illum ullum, ad mel dolores iudicabit definitiones, ad vel sapientem.</p>
        <span class="btn">Read more</span>
      </article>
      <article class="post">
        <h3>Quam nihil facilis qui ad, malorum veritus graecis an per mundi. Ius te</h3>
        <p>Partem melius pertinacia et sed, no vero aliquam fabulas. Summo vocibus scripserit ex vel, per recteque ancillae eu. Quo nemore menandri complectitur no, quas eloquentiam ad quo. Ne has illum ullum, ad mel dolores iudicabit definitiones, ad vel sapientem.</p>
        <span class="btn">Read more</span>
      </article>
      <article class="post">
        <h3>Quam nihil facilis qui ad, malorum veritus graecis an per mundi. Ius te</h3>
        <p>Partem melius pertinacia et sed, no vero aliquam fabulas. Summo vocibus scripserit ex vel, per recteque ancillae eu. Quo nemore menandri complectitur no, quas eloquentiam ad quo. Ne has illum ullum, ad mel dolores iudicabit definitiones, ad vel sapientem.</p>
        <span class="btn">Read more</span>
      </article>
    </div>
  </div>
</section>

<section class="stories">
  <div class="wrap">
    <h2 class="section-title">Our Success Stories</h2>
    <div class="story">
      <div class="story-photo" role="img" aria-label="Group photo of graduating students standing beside their motorcycles outdoors"></div>
      <div class="story-text">
        <h3>Temporibus autem quibusdam et aut officiis debitis aut rerum necessitatibus saepe</h3>
        <p>Temporibus autem quibusdam et aut officiis debitis aut rerum necessitatibus saepe eveniet ut et voluptates repudiandae sint et molestiae non recusandae. Itaque earum rerum hic tenetur a sapiente delectus, ut aut reiciendis voluptatibus maiores alias consequatur aut perferendis doloribus asperiores repellat.</p>
        <p>Nam libero tempore, cum soluta nobis est eligendi optio cumque nihil impedit quo minus id quod maxime placeat facere possimus, omnis voluptas assumenda est, omnis dolor repellendus. Sed ut perspiciatis unde omnis iste natus error sit voluptatem accusantium.</p>
        <span class="btn">Read more</span>
      </div>
    </div>
  </div>
</section>

<footer class="site-footer">
  <div class="wrap footer-cols">
    <div class="footer-col">
      <h4>Navigation</h4>
      <ul><li>Home</li><li>About Us</li><li>Our Staff</li><li>Our Fleet</li><li>Client Testimonials</li><li>Friends of Ridexa</li><li>Course Descriptions</li><li>Course Pricing</li></ul>
    </div>
    <div class="footer-col">
      <h4>Connect With Us</h4>
      <div class="social"><span></span><span></span><span></span><span></span><span></span><span></span></div>
    </div>
    <div class="footer-col">
      <h4>Share your thoughts!</h4>
      <p>Tell us about your training experience or ask us anything. Leave your email and we will get back to you shortly.</p>
      <div class="footer-form"><span class="field">Email Address</span><span class="btn">Send</span></div>
    </div>
    <div class="footer-col">
      <h4>Contact Us</h4>
      <p>Ridexa Academy<br>Ridgeford, Northvale<br>555-0147</p>
    </div>
  </div>
  <div class="footer-bottom">
    <div class="wrap"><span>Site Map &nbsp;|&nbsp; Privacy Policy &nbsp;|&nbsp; Legal</span><span>Copyright 2016 Ridexa Academy. All Rights Reserved.</span></div>
  </div>
</footer>

</body>
</html>
```